Need simple and modern looking business card with all my information on one side and logo on the other side
Info :
Company name - VELMAR CONSTRUCTION LLC
Company addres- 418 harbor 87th. Dunmoor park ny 10352
Email- velmarllc@tridomail.Com
Company phone number 555-318-6094
Cell number- 555-742-0583
Web site - velmarllc.Com
My name Gerald tomasino

Target Market(s)

Construction , home improvement, remodeling

Industry/Entity Type

Construction

Contact Information for Business Card

It has to be moder but at the same time simple

Font styles to use
Sans Serif

Colors
0255a3
ffffff
000000
f78f20
b1b1b1
9d9d9d
1b1b1b
33a6d7
ec1f27

Requirements
Must have
• My logo on one side maybe with a some kind of background on the other side all my information
Nice to have
• Some kind of background pictures provided by you .PLEASE HAVE ACCOUNT WITH PIXELVAULT WILL NOT PAY ANY EXTRA FEES .
Should not have
• Any kind of hamer, nails,screws, helmets itp. Please do not copy the other designs come up with something new.

```html
<!DOCTYPE html>
<html lang="en">
<head>
<meta charset="utf-8">
<title>Velmar Construction LLC – Business Card</title>
<link rel="stylesheet" href="https://fonts.googleapis.com/css2?family=Jost:wght@400;500&display=swap">
<style>
  :root {
    --orange: #f78f20;
    --ink: #1b1b1b;
    --white: #ffffff;
    --backdrop: #e9eeec;
    --rule: #f78f20;
  }
  * { margin: 0; padding: 0; box-sizing: border-box; }
  html, body {
    width: 1200px;
    height: 800px;
    overflow: hidden;
  }
  body {
    background: var(--backdrop);
    font-family: "Jost", sans-serif;
    color: var(--ink);
    display: flex;
    align-items: center;
    justify-content: center;
    gap: 40px;
  }
  .card {
    width: 560px;
    height: 320px;
    position: relative;
    box-shadow: 0 10px 24px rgba(0,0,0,0.12);
  }

  /* Info side */
  .card--info {
    background: var(--white);
    text-align: right;
    padding: 40px 44px 0 0;
  }
  .holder-name {
    color: var(--orange);
    font-size: 22px;
    font-weight: 400;
    line-height: 1.1;
  }
  .holder-mobile {
    font-size: 24px;
    font-weight: 400;
    line-height: 1.25;
    letter-spacing: 0.5px;
  }
  .divider {
    position: absolute;
    left: 150px;
    right: 36px;
    top: 118px;
    height: 4px;
    background: var(--rule);
  }
  .company-block {
    margin-top: 42px;
    font-size: 15px;
    line-height: 1.45;
  }
  .company-name {
    font-size: 22px;
    font-weight: 400;
    letter-spacing: 0.5px;
    line-height: 1.2;
    margin-bottom: 2px;
  }
  .company-name .initial { color: var(--orange); }
  .company-web { color: var(--orange); }

  /* Logo side */
  .card--logo {
    background: var(--orange);
    display: flex;
    align-items: center;
    justify-content: center;
  }
  .logo-panel {
    width: 410px;
    height: 250px;
    background: var(--white);
    padding: 20px;
  }
  .logo-frame {
    width: 100%;
    height: 100%;
    border: 1.5px solid var(--orange);
    display: flex;
    align-items: center;
    justify-content: center;
    gap: 14px;
  }
  .logo-square {
    width: 22px;
    height: 22px;
    background: var(--orange);
    flex-shrink: 0;
  }
  .logo-name {
    font-size: 24px;
    font-weight: 500;
    letter-spacing: 1px;
    color: var(--ink);
  }
</style>
</head>
<body>
  <section class="card card--info" aria-label="Contact side">
    <p class="holder-name">Gerald tomasino</p>
    <p class="holder-mobile">M : 555-742-0583</p>
    <div class="divider"></div>
    <div class="company-block">
      <p class="company-name"><span class="initial">V</span>ELMAR CONSTRUCTION LLC</p>
      <p class="company-address">418 harbor 87th. Dunmoor park ny 10352</p>
      <p class="company-email">Email- velmarllc@tridomail.Com</p>
      <p class="company-phone">Phone number : 555-318-6094</p>
      <p class="company-web">Web site - velmarllc.Com</p>
    </div>
  </section>

  <section class="card card--logo" aria-label="Logo side">
    <div class="logo-panel">
      <div class="logo-frame">
        <span class="logo-square"></span>
        <span class="logo-name">VELMAR CONSTRUCTION LLC</span>
      </div>
    </div>
  </section>
</body>
</html>
```